Mortgage Loan officer needs clean/modern business card design

Looking for a clean, modern 2-sided business card design. We like the earth tones used in our logo and website http://varnhill-lending.com . Would also like to incorporate: 1) Something special to make our card stand out - a pop of color or embossed logo, for instance and 2) please include "Mortgage Loans" "Reverse Mortgages" "Private Money Loans" on back of card with the logo.

Front: Needs to include agent/company license info - see website. Agent name: Marco Lindqvist

Here are fonts and colors used for our logo:
Font: Avenir Next
Colors:
#2c3539 - Dark Gray
#576870 - Light Gray
#ffffff - Background White

Target Market(s)

Prospects and current clients. Will also be distributing to people in professional network (attorneys and CPAs)

Industry/Entity Type

Business

Contact Information for Business Card

Include agent name, contact info, website on front, licensing info for agent an company. Logo and services offered on back

Font styles to use
Other font styles liked:
• Avenir Next

Requirements
Must have
• See project description
Should not have
• Nothing cheesy

```html
<!DOCTYPE html>
<html lang="en">
<head>
<meta charset="utf-8">
<title>Varnhill Lending Group – Business Card</title>
<link href="https://fonts.googleapis.com/css2?family=Montserrat:wght@600;700&family=Nunito+Sans:wght@300;400;600&display=swap" rel="stylesheet">
<style>
  :root {
    --dark-gray: #2c3539;
    --light-gray: #576870;
    --white: #ffffff;
    --backdrop: #6b6e70;
    --soft-text: #c9d0d3;
  }
  * { box-sizing: border-box; margin: 0; padding: 0; }
  html, body {
    width: 1200px; height: 900px; overflow: hidden;
    background: var(--backdrop);
    font-family: "Nunito Sans", sans-serif;
  }
  .card {
    position: absolute;
    width: 600px; height: 343px;
    border-radius: 26px;
    overflow: hidden;
    background: var(--dark-gray);
    box-shadow: 0 14px 30px rgba(0,0,0,.35);
  }
  .card--back { left: 300px; top: 60px; }
  .card--front { left: 300px; top: 470px; }

  /* Back side */
  .brand-circle {
    position: absolute;
    border-radius: 50%;
    display: flex; align-items: center; justify-content: center;
    text-align: center;
  }
  .card--back .brand-circle {
    left: 225px; top: 26px; width: 150px; height: 150px;
    border: 1.5px solid var(--white);
    color: var(--white);
  }
  .brand-name {
    font-family: "Nunito Sans", sans-serif;
    font-weight: 400;
    font-size: 19px;
    line-height: 1.2;
  }
  .services {
    position: absolute; left: 0; right: 0; top: 232px;
    text-align: center;
    color: var(--white);
    font-size: 13px; font-weight: 600;
  }
  .license {
    position: absolute; left: 0; right: 0; top: 262px;
    text-align: center;
    color: var(--soft-text);
    font-size: 14.5px; font-weight: 300;
    letter-spacing: .2px;
  }

  /* Front side */
  .front-shape { position: absolute; inset: 0; }
  .card--front .brand-circle {
    left: 72px; top: 96px; width: 160px; height: 160px;
    border: 1.5px solid var(--dark-gray);
    color: var(--light-gray);
  }
  .agent {
    position: absolute; left: 365px; top: 58px;
    color: var(--white);
  }
  .agent-name {
    font-family: "Montserrat", sans-serif;
    font-weight: 700; font-size: 24px; letter-spacing: .3px;
  }
  .agent-title {
    font-family: "Montserrat", sans-serif;
    font-weight: 600; font-size: 12px; letter-spacing: .5px;
    margin-top: 2px;
  }
  .address {
    margin-top: 18px;
    font-size: 14px; font-weight: 300; line-height: 1.45;
    color: var(--soft-text);
  }
  .contact-list {
    list-style: none;
    margin-top: 16px;
    font-size: 14px; font-weight: 300;
    color: var(--soft-text);
  }
  .contact-list li {
    display: flex; align-items: center; gap: 12px;
    height: 23px;
  }
  .contact-list svg { width: 13px; height: 13px; flex: none; }
</style>
</head>
<body>

<section class="card card--back" aria-label="Card back">
  <div class="brand-circle"><span class="brand-name">Varnhill<br>Lending Group</span></div>
  <p class="services">"Mortgage Loans | Reverse Mortgages | Private Money Loans"</p>
  <p class="license">License: NMLS:400125 DRE:02216437 CO. DRE:02250913/NMLS:418806</p>
</section>

<section class="card card--front" aria-label="Card front">
  <svg class="front-shape" viewBox="0 0 600 343" preserveAspectRatio="none">
    <path d="M0 0 H300 C372 70 384 250 312 343 H0 Z" fill="var(--white)"/>
    <path d="M318 -4 C392 70 402 250 332 347" fill="none" stroke="var(--light-gray)" stroke-width="9"/>
  </svg>

  <div class="brand-circle"><span class="brand-name">Varnhill<br>Lending Group</span></div>

  <div class="agent">
    <h1 class="agent-name">MARCO LINDQVIST</h1>
    <p class="agent-title">LOAN OFFICER</p>
    <p class="address">2280 Harbor Row, Suite 310,<br>Fremont, CA 94538</p>
    <ul class="contact-list">
      <li>
        <svg viewBox="0 0 16 16" fill="none" stroke="currentColor" stroke-width="1.4"><path d="M4 1.5h3l1 3.5-2 1.2a8 8 0 0 0 3.8 3.8L11 8l3.5 1v3a2 2 0 0 1-2 2A11 11 0 0 1 2 3.5a2 2 0 0 1 2-2z"/></svg>
        510-555-0142
      </li>
      <li>
        <svg viewBox="0 0 16 16" fill="none" stroke="currentColor" stroke-width="1.4"><rect x="4" y="1" width="8" height="14" rx="1.5"/><line x1="7" y1="12.5" x2="9" y2="12.5"/></svg>
        510-555-0187
      </li>
      <li>
        <svg viewBox="0 0 16 16" fill="none" stroke="currentColor" stroke-width="1.4"><rect x="2" y="6" width="12" height="7" rx="1"/><rect x="4.5" y="2" width="7" height="4"/><line x1="5" y1="10" x2="11" y2="10"/></svg>
        510-555-0163
      </li>
      <li>
        <svg viewBox="0 0 16 16" fill="none" stroke="currentColor" stroke-width="1.3"><circle cx="8" cy="8" r="6.5"/><ellipse cx="8" cy="8" rx="3" ry="6.5"/><line x1="1.5" y1="8" x2="14.5" y2="8"/></svg>
        www.varnhill-lending.com
      </li>
    </ul>
  </div>
</section>

</body>
</html>
```